Website Refresh of vorlith-mx.example

INTRODUCTION: The Regional Growth Alliance of Upper Basinfield (RGAUB) is a 501-C3 nonprofit regional economic development organization with the goals of creating jobs, strengthening, and supporting existing business, and increasing wealth and prosperity of the region. RGAUB is a private/public consortium funded by the nine sectors of the region with membership from large employers, small businesses, utilities, educational institutions, non‐profits, city government, county government, financial institutions, and developers/real estate/contractors. Our region consists of Basinfield, Winslow, Sedona and Camp Verde and all of Coconino County.

MISSION: “With our partners, we provide quality economic growth for Upper Basinfield.”

PROJECT & DESCRIPTION: We are hoping to revitalize and strengthen our brand, creating a cohesive and impactful identity that resonates with our target audience. Utilization of recent strategic data should be incorporated to invoke personal, emotional, and genuine elements into promotional activities, ensuring that marketing strategies resonate on a human level rather than feeling impersonal or automated. Collaborating with our team to understand key messaging is imperative. Communicating who we are, what we do and why it’s important is key.
WEBSITE: Update the existing website for a comprehensive refresh. Our goal is to enhance the user experience, modernize the design and improve functionality to better align with our brand and goals outlined in the strategic plan.
The website should do the following:
• Engage website visitors with fresh and updated content.
• Capture website visitors and convert them into a lead.
• Refresh current website with more photo rich content.
• Create a page that shows available buildings or land options.
• Create a search function.
• Ensure mobile friendliness.
• Ensure that the website is user friendly.
Create a feature that allows us to upload properties in the region for sale or lease.

Please see the attached new logo which has yet to be launched as we want to roll it out with the website refresh. We are open to other features that you feel our website should have. Please also see our attached strategic roadmap.

```html
<!DOCTYPE html>
<html lang="en">
<head>
<meta charset="utf-8">
<title>RGAUB — Regional Growth Alliance of Upper Basinfield</title>
<link href="https://fonts.googleapis.com/css2?family=Montserrat:wght@400;500;600;700;800&display=swap" rel="stylesheet">
<style>
:root{
  --navy:#13285a;
  --blue:#2f6fb7;
  --sky:#3d8ac6;
  --sky-light:#5aa6dc;
  --orange:#d9601c;
  --ink:#1a1f36;
  --grey:#6b6f7a;
  --line:#d8dbe0;
  --faint:#eef0f2;
  --white:#ffffff;
}
*{box-sizing:border-box;margin:0;padding:0}
html,body{width:1200px;height:4307px;overflow:hidden;background:var(--white)}
body{font-family:'Montserrat',sans-serif;color:var(--ink);position:relative}
.abs{position:absolute}
.btn{position:absolute;background:var(--orange);color:var(--white);font-weight:600;font-size:12px;display:flex;align-items:center;justify-content:center;letter-spacing:.3px}
.h2{position:absolute;left:0;width:1200px;text-align:center;font-weight:800;color:var(--navy);font-size:30px;letter-spacing:.5px}
.ghost{position:absolute;left:0;width:1200px;text-align:center;font-weight:800;color:var(--faint);letter-spacing:2px}

/* header */
.site-header{position:absolute;top:0;left:0;width:1200px;height:62px;background:var(--white)}
.nav{position:absolute;top:24px;font-size:11px;font-weight:600;color:var(--navy)}
.brand{position:absolute;left:508px;top:0;width:180px;height:80px;background:var(--blue);border:3px solid var(--white);outline:1px solid var(--blue);display:flex;flex-direction:column;align-items:center;justify-content:center;color:var(--white);z-index:3}
.brand-name{font-size:30px;font-weight:700;letter-spacing:1px;line-height:1}
.brand-tag{font-size:5px;font-weight:500;margin-top:6px;letter-spacing:.2px}

/* hero */
.hero{position:absolute;top:62px;left:0;width:1200px;height:666px}
.hero-photo{position:absolute;inset:0;background:linear-gradient(180deg,#3f74b5 0%,#7ba8d6 32%,#7d8a93 48%,#6d6a5e 62%,#8b7c6a 80%,#5a5650 100%)}
.hero h1{position:absolute;left:0;width:1200px;text-align:center;color:var(--white);font-weight:700;line-height:1}
.hero p{position:absolute;left:0;width:1200px;text-align:center;color:var(--white);font-size:13.5px;line-height:18px}
.search{position:absolute;left:391px;top:305px;width:272px;height:38px;background:var(--white);font-size:11px;color:var(--ink);padding:12px 12px}
.search-btn{position:absolute;right:0;top:0;width:38px;height:38px;background:var(--blue)}

/* services */
.svc-title{font-size:14px;font-weight:600;color:var(--navy);text-align:center;position:absolute;width:220px;line-height:17px}
.svc-text{font-size:10px;color:var(--grey);text-align:center;position:absolute;width:190px;line-height:13px}
.icon{position:absolute;border-radius:50%;background:var(--blue)}
.arrow-dot{position:absolute;width:24px;height:24px;border-radius:50%;background:var(--orange)}

/* about */
.about{position:absolute;top:1193px;left:0;width:1200px;height:492px;background:var(--sky);overflow:hidden}
.about h2{position:absolute;left:678px;top:70px;color:var(--white);font-size:30px;line-height:37px;font-weight:800}
.about p{position:absolute;left:680px;width:380px;color:var(--white);font-size:10.5px;line-height:17px}

/* board */
.member{position:absolute;width:200px;text-align:center}
.member .pic{width:140px;height:140px;border-radius:50%;margin:0 auto;background:linear-gradient(180deg,#c9ccd2,#5c6170)}
.member h4{font-size:15px;font-weight:500;margin-top:14px;color:var(--ink)}
.member small{display:block;font-size:10px;color:var(--grey);line-height:14px;margin-top:3px}

/* blog */
.card{position:absolute;top:2238px;width:306px;height:352px;border-left:2px solid var(--sky-light);background:var(--white)}
.card .img{height:240px}
.card h5{font-size:14.5px;font-weight:500;margin:16px 28px 0 18px;line-height:18px}
.card p{font-size:10px;color:var(--grey);margin:6px 40px 0 18px;line-height:16px}
.card .arrow-dot{right:10px;top:310px}
.date{position:absolute;left:-14px;top:-20px;width:54px;height:54px;border-radius:50%;background:var(--white);text-align:center;font-size:9px;font-weight:700;color:var(--navy);padding-top:6px;line-height:10px}
.date span{display:block;margin:3px auto 0;width:40px;background:var(--blue);color:var(--white);border-radius:8px;font-size:9px;padding:2px 0}

/* industries */
.ind-label{position:absolute;width:170px;text-align:center;font-size:15px;font-weight:500;color:var(--ink);line-height:16px}

/* housing */
.housing{position:absolute;left:122px;top:3228px;width:956px;height:348px;background:var(--orange);overflow:hidden}
.housing h3{position:absolute;left:588px;top:60px;color:var(--white);font-size:47px;line-height:56px;font-weight:800}

/* footer */
.footer{position:absolute;left:0;top:3990px;width:1200px;height:317px}
.footer h6{position:absolute;top:72px;color:var(--white);font-size:13px;font-weight:600;letter-spacing:.3px}
.f-text{position:absolute;color:var(--white);font-size:8.5px;line-height:13px}
.f-link{position:absolute;color:var(--white);font-size:8.5px}
.f-ico{position:absolute;width:22px;height:22px;border-radius:50%;border:1px solid var(--white)}
</style>
</head>
<body>

<header class="site-header">
  <span class="nav" style="left:122px">DOING BUSINESS HERE</span>
  <span class="nav" style="left:266px">LIVING HERE</span>
  <span class="nav" style="left:354px">RESOURCES &amp; DATA</span>
  <span class="nav" style="left:721px">TALENT &amp; WORKFORC</span>
  <span class="nav" style="left:861px">ABOUT RGAUB</span>
  <span class="btn" style="left:964px;top:13px;width:113px;height:37px;font-size:11px">CONTACT US</span>
</header>
<div class="brand"><span class="brand-name">RGAUB</span><span class="brand-tag">REGIONAL GROWTH ALLIANCE OF UPPER BASINFIELD</span></div>

<section class="hero">
  <div class="hero-photo" role="img" aria-label="Aerial photo of the town with snow-capped mountains under a blue sky"></div>
  <svg class="abs" style="left:0;top:0" width="1200" height="666" viewBox="0 0 1200 666">
    <polygon points="0,666 1200,526 1200,600 1100,666" fill="#fff"/>
    <polygon points="0,666 0,640 1030,527 1200,610 1200,680" fill="#d9601c"/>
    <polygon points="0,666 1050,543 1200,612 1200,666" fill="#fff"/>
  </svg>
  <h1 style="top:90px;font-size:62px;letter-spacing:2px">INNOVATING</h1>
  <h1 style="top:152px;font-size:42px">ECONOMIC FUTURES FOR</h1>
  <h1 style="top:200px;font-size:42px">UPPER BASINFIELD</h1>
  <p style="top:252px">RGAUB is an economic collaborative organization supporte<br>by a multitude of agencies in Upper Basinfield.</p>
  <div class="search">I would like to...
    <div class="search-btn"><svg width="38" height="38" viewBox="0 0 38 38"><circle cx="18" cy="18" r="6" fill="none" stroke="#fff" stroke-width="2"/><line x1="22" y1="22" x2="27" y2="27" stroke="#fff" stroke-width="2"/></svg></div>
  </div>
  <span class="btn" style="left:673px;top:305px;width:135px;height:38px">GET STARTED</span>
</section>

<!-- services -->
<h2 class="h2" style="top:717px">OUR SERVICES</h2>
<svg class="abs" style="left:0;top:760px" width="1200" height="340" viewBox="0 760 1200 340">
  <defs><linearGradient id="dg" x1="0" y1="0" x2="0" y2="1"><stop offset="0" stop-color="#fff"/><stop offset="1" stop-color="#e6e8eb"/></linearGradient></defs>
  <line x1="0" y1="925" x2="1200" y2="925" stroke="#d8dbe0"/>
  <polygon points="310,770 456,925 310,1080 164,925" fill="url(#dg)" stroke="#d8dbe0"/>
  <polygon points="598,770 744,925 598,1080 452,925" fill="url(#dg)" stroke="#d8dbe0"/>
  <polygon points="888,770 1034,925 888,1080 742,925" fill="url(#dg)" stroke="#d8dbe0"/>
</svg>
<div class="icon" style="left:274px;top:828px;width:72px;height:72px"><svg width="72" height="72"><rect x="24" y="40" width="5" height="9" fill="#fff"/><rect x="32" y="34" width="5" height="15" fill="#fff"/><rect x="40" y="28" width="5" height="21" fill="#fff"/><polyline points="22,36 34,28 46,22" fill="none" stroke="#fff" stroke-width="2"/></svg></div>
<div class="icon" style="left:562px;top:828px;width:72px;height:72px"><svg width="72" height="72"><circle cx="36" cy="32" r="10" fill="none" stroke="#fff" stroke-width="3"/><rect x="24" y="44" width="24" height="4" fill="#fff"/><rect x="26" y="50" width="20" height="3" fill="#fff"/></svg></div>
<div class="icon" style="left:852px;top:828px;width:72px;height:72px"><svg width="72" height="72"><circle cx="36" cy="26" r="6" fill="#fff"/><path d="M22 44 q14 10 28 0 v6 h-28z" fill="#fff"/><path d="M28 38 h16 v4 h-16z" fill="#fff"/></svg></div>
<div class="svc-title" style="left:200px;top:912px">Business<br>Attraction</div>
<div class="svc-title" style="left:488px;top:912px">Workforce<br>Development</div>
<div class="svc-title" style="left:778px;top:912px">Business Retention<br>&amp; Expansion</div>
<div class="svc-text" style="left:215px;top:953px">Creating more jobs is the key to increasing economic prosperity and vitality in the region.</div>
<div class="svc-text" style="left:503px;top:953px">Strategic workforce development, combined with efforts to bring more high-paying jobs to our region.</div>
<div class="svc-text" style="left:793px;top:953px">Creating more jobs is the key to increasing economic prosperity and vitality in the region.</div>
<div class="arrow-dot" style="left:298px;top:1064px"><svg width="24" height="24"><path d="M7 12h10M13 8l4 4-4 4" stroke="#fff" stroke-width="2" fill="none"/></svg></div>
<div class="arrow-dot" style="left:586px;top:1064px"><svg width="24" height="24"><path d="M7 12h10M13 8l4 4-4 4" stroke="#fff" stroke-width="2" fill="none"/></svg></div>
<div class="arrow-dot" style="left:876px;top:1064px"><svg width="24" height="24"><path d="M7 12h10M13 8l4 4-4 4" stroke="#fff" stroke-width="2" fill="none"/></svg></div>
<div class="ghost" style="top:1090px;font-size:104px">OUR SERVICES</div>

<!-- about -->
<section class="about">
  <svg class="abs" style="left:0;top:0" width="1200" height="492">
    <polygon points="30,492 300,40 565,492" fill="#5aa6dc" opacity=".55"/>
    <polyline points="1200,180 1112,260 1200,340" fill="none" stroke="#7fbbe6" stroke-width="1.5"/>
  </svg>
  <div class="abs" style="left:112px;top:100px;width:360px;height:360px;border-radius:50%;background:var(--white)"></div>
  <div class="abs" role="img" aria-label="Portrait of the alliance president in front of a brick building" style="left:124px;top:112px;width:336px;height:336px;border-radius:50%;background:linear-gradient(160deg,#8a5a3c,#3a2a28 55%,#1c2440);overflow:hidden">
    <div class="abs" style="left:0;top:250px;width:336px;height:50px;background:linear-gradient(90deg,#13285a,#2f6fb7)"></div>
    <div class="abs" style="left:106px;top:178px;color:#fff;font-size:26px;font-weight:700">MAREN TOLLIVER</div>
    <div class="abs" style="left:150px;top:208px;color:#fff;font-size:8px;letter-spacing:4px">PRESIDENT / CEO</div>
  </div>
  <div class="abs" style="left:276px;top:264px;width:56px;height:56px;border-radius:50%;background:var(--white)"><svg width="56" height="56"><polygon points="22,17 40,28 22,39" fill="#d9601c"/></svg></div>
  <div class="abs" role="img" aria-label="Historic brick downtown building" style="left:405px;top:201px;width:144px;height:144px;border-radius:50%;border:4px solid #fff;background:linear-gradient(180deg,#8fb5dc,#8a4a34 55%,#5a3a2c)"></div>
  <h2>ABOUT&nbsp; REGIONAL<br>GROWTH ALLIANCE OF<br>UPPER BASINFIELD</h2>
  <p style="top:186px">RGAUB is an economic collaborative organization supported by a multitude of agencies in Upper Basinfield. RGAUB coordinates the regional efforts of private, public, and nonprofit organizations that are working to improve economic vitality in our area.</p>
  <p style="top:272px">RGAUB provides insight, infrastructure, resources, and development efforts to enhance the economic prosperity of the region by increasing wealth and accelerating job creation. We actively pursue new business to the region while supporting existing businesses to grow and expand. Together with our partners, we provide quality economic growth for Upper Basinfield.</p>
  <span class="btn" style="left:680px;top:384px;width:136px;height:40px">READ MORE</span>
</section>

<!-- board -->
<h2 class="h2" style="top:1730px;line-height:38px">EXECUTIVE BOARD, ADVISORY<br>COMMITTEE &amp; FOUNDERS</h2>
<div class="member" style="left:93px;top:1830px"><div class="pic" role="img" aria-label="Headshot of board member"></div><h4>Maren Tolliver</h4><small>President &amp; CEO</small></div>
<div class="member" style="left:296px;top:1830px"><div class="pic" role="img" aria-label="Headshot of board member"></div><h4>Calder Venn</h4><small>Basinfield State University<br>Associate Vice President</small></div>
<div class="member" style="left:498px;top:1830px"><div class="pic" role="img" aria-label="Headshot of board member"></div><h4>Rosalyn Pike</h4><small>Economic Vitality<br>Director</small></div>
<div class="member" style="left:702px;top:1828px"><div class="pic" role="img" aria-label="Headshot of board member"></div><h4>Thaddeus Orrin</h4><small>President &amp; CEO Basinfield<br>Health Network</small></div>
<div class="member" style="left:901px;top:1828px"><div class="pic" role="img" aria-label="Headshot of board member"></div><h4>Celia Brandt</h4><small>HR Director, Operations &amp;<br>Supply Chain - Halvern Medical</small></div>
<svg class="abs" style="left:0;top:2088px" width="1200" height="2"><line x1="0" y1="1" x2="1200" y2="1" stroke="#d8dbe0"/></svg>
<span class="btn" style="left:527px;top:2070px;width:146px;height:42px">MEET OUR TEEM</span>

<!-- blog -->
<h2 class="h2" style="top:2160px">RECENT BLOG POSTS</h2>
<article class="card" style="left:141px">
  <div class="img" role="img" aria-label="Aerial view of a university campus with mountains" style="background:linear-gradient(180deg,#7da6d0,#6f7c6e 45%,#4c5a4a)"></div>
  <div class="date">5<br>JUNE<span>2025</span></div>
  <h5>The Power of a Thriving University</h5>
  <p>My heart sank as I read the article in the daily paper. My alma mater, the lakeside campus of a state college ...</p>
  <div class="arrow-dot"><svg width="24" height="24"><path d="M7 12h10M13 8l4 4-4 4" stroke="#fff" stroke-width="2" fill="none"/></svg></div>
</article>
<article class="card" style="left:466px">
  <div class="img" role="img" aria-label="Two people working at a laptop in an office" style="background:linear-gradient(160deg,#8a7968,#5e5a58 50%,#9aa4ae)"></div>
  <div class="date">15<br>JUNE<span>2025</span></div>
  <h5>Ridgeline Power Business Tools to Lower Energy Costs</h5>
  <p>As temperatures heat up, it's important for businesses to explore ways to save on their energy bills...</p>
  <div class="arrow-dot"><svg width="24" height="24"><path d="M7 12h10M13 8l4 4-4 4" stroke="#fff" stroke-width="2" fill="none"/></svg></div>
</article>
<article class="card" style="left:790px">
  <div class="img" role="img" aria-label="Group of delegates posing in a meeting room" style="background:linear-gradient(180deg,#c7bfb2,#6d6660 60%,#3b3a40)"></div>
  <div class="date">13<br>APRIL<span>2025</span></div>
  <h5>State Commerce Council Tours Upper Basinfield</h5>
  <p>It is always a joy showing off all that our region has to offer – and what new things are on the horizon – to visitors...</p>
  <div class="arrow-dot"><svg width="24" height="24"><path d="M7 12h10M13 8l4 4-4 4" stroke="#fff" stroke-width="2" fill="none"/></svg></div>
</article>
<div class="ghost" style="top:2590px;font-size:122px">RECENT BLOG</div>
<span class="btn" style="left:546px;top:2685px;width:146px;height:42px">VIEW ALL BLOG</span>

<!-- industries -->
<h2 class="h2" style="top:2774px">INDASTRY WE SERVE</h2>
<svg class="abs" style="left:0;top:2800px" width="1200" height="380" viewBox="0 2800 1200 380">
  <defs>
    <linearGradient id="ig" x1="0" y1="0" x2="0" y2="1"><stop offset="0" stop-color="#fff"/><stop offset="1" stop-color="#dfe2e6"/></linearGradient>
    <linearGradient id="ib" x1="0" y1="0" x2="0" y2="1"><stop offset="0" stop-color="#2f6fb7"/><stop offset="1" stop-color="#7fa9d3"/></linearGradient>
  </defs>
  <g stroke="#d3d6db" fill="url(#ig)">
    <polygon points="242,2810 345,2913 242,3016 139,2913"/>
    <polygon points="431,2810 534,2913 431,3016 328,2913"/>
    <polygon points="807,2810 910,2913 807,3016 704,2913"/>
    <polygon points="994,2810 1097,2913 994,3016 891,2913"/>
    <polygon points="337,2937 440,3040 337,3143 234,3040"/>
    <polygon points="523,2937 626,3040 523,3143 420,3040"/>
    <polygon points="711,2937 814,3040 711,3143 608,3040"/>
    <polygon points="898,2937 1001,3040 898,3143 795,3040"/>
  </g>
  <polygon points="618,2810 721,2913 618,3016 515,2913" fill="url(#ib)"/>
</svg>
<div class="icon" style="left:216px;top:2878px;width:52px;height:52px"></div>
<div class="icon" style="left:405px;top:2874px;width:52px;height:52px"></div>
<div class="icon" style="left:592px;top:2874px;width:52px;height:52px;background:#fff"><svg width="52" height="52"><rect x="16" y="20" width="20" height="14" rx="2" fill="#2f6fb7"/><rect x="22" y="16" width="8" height="5" fill="none" stroke="#2f6fb7" stroke-width="2"/></svg></div>
<div class="icon" style="left:781px;top:2874px;width:52px;height:52px"></div>
<div class="icon" style="left:968px;top:2878px;width:52px;height:52px"><svg width="52" height="52"><polyline points="16,32 23,25 29,30 37,20" stroke="#fff" stroke-width="3" fill="none"/></svg></div>
<div class="icon" style="left:311px;top:3002px;width:52px;height:52px"></div>
<div class="icon" style="left:497px;top:3000px;width:52px;height:52px"></div>
<div class="icon" style="left:685px;top:3000px;width:52px;height:52px"></div>
<div class="icon" style="left:872px;top:3000px;width:52px;height:52px"></div>
<div class="ind-label" style="left:157px;top:2940px">Educational<br>Institutions</div>
<div class="ind-label" style="left:346px;top:2940px">County<br>Government</div>
<div class="ind-label" style="left:533px;top:2940px;color:#fff">Small<br>Businesses</div>
<div class="ind-label" style="left:722px;top:2946px">Utilities</div>
<div class="ind-label" style="left:909px;top:2948px">Non-Profits</div>
<div class="ind-label" style="left:252px;top:3066px">City<br>Government</div>
<div class="ind-label" style="left:438px;top:3064px">Large<br>Employers</div>
<div class="ind-label" style="left:626px;top:3066px">Financial<br>Institutions</div>
<div class="ind-label" style="left:813px;top:3066px">Developers<br>Real Estat<br>Contractors</div>

<!-- housing -->
<section class="housing">
  <svg class="abs" style="left:0;top:0" width="956" height="348"><polygon points="300,348 520,0 956,0 956,348" fill="#e26a24" opacity=".5"/></svg>
  <div class="abs" role="img" aria-label="Cover of the workforce housing report booklet" style="left:70px;top:40px;width:270px;height:250px;background:linear-gradient(160deg,#ffffff,#e3e6ea);transform:rotate(14deg);box-shadow:0 10px 24px rgba(0,0,0,.3)"></div>
  <h3>GET YOUR<br>HOUSING<br>REPORT</h3>
  <span class="btn" style="left:598px;top:258px;width:152px;height:40px;background:#fff;color:var(--navy)">DOWNLOAD HERE</span>
</section>

<!-- question -->
<div class="abs" style="left:0;top:3576px;width:1200px;height:420px;background:linear-gradient(180deg,#fff 0%,#fff 30%,#cfe0f1 62%,#8aa3be 78%,#6d7569 100%)" role="img" aria-label="Panorama of the town and mountain range"></div>
<h2 class="h2" style="top:3620px;font-size:40px;line-height:52px">GOT A QUESTION OR<br>COMMENT TO SEND OUR WAY?</h2>
<span class="btn" style="left:523px;top:3738px;width:134px;height:40px">CONTACT US</span>

<!-- footer -->
<footer class="footer">
  <svg class="abs" style="left:0;top:0" width="1200" height="317"><polygon points="0,50 300,40 700,0 1200,30 1200,317 0,317" fill="#13285a"/><line x1="122" y1="292" x2="1077" y2="292" stroke="#3a4d7a"/></svg>
  <div class="abs" style="left:122px;top:72px;width:146px;height:66px;border:2px solid #fff;background:var(--blue);display:flex;flex-direction:column;align-items:center;justify-content:center;color:#fff"><span style="font-size:26px;font-weight:700;line-height:1">RGAUB</span><span style="font-size:4.5px;margin-top:5px">REGIONAL GROWTH ALLIANCE OF UPPER BASINFIELD</span></div>
  <div class="f-text" style="left:122px;top:150px;width:160px">RGAUB is an economic collaborative organization supported by a multitude of agencies in Upper Basinfield</div>
  <div class="f-ico" style="left:126px;top:195px"></div><div class="f-ico" style="left:155px;top:195px"></div><div class="f-ico" style="left:184px;top:195px"></div>

  <h6 style="left:315px">CONTACT US</h6>
  <div class="f-ico" style="left:326px;top:100px"><svg width="20" height="20"><path d="M7 5l2 3-1.5 1.5a7 7 0 0 0 3 3L12 11l3 2-1 2c-5 0-9-4-9-9z" fill="#fff"/></svg></div>
  <div class="f-link" style="left:360px;top:106px">(555) 014-2870</div>
  <div class="f-ico" style="left:326px;top:133px"><svg width="20" height="20"><rect x="5" y="6" width="10" height="8" fill="#fff"/></svg></div>
  <div class="f-link" style="left:360px;top:139px;color:#6fb2e6">vorlith-mx.example</div>
  <div class="f-ico" style="left:326px;top:166px"><svg width="20" height="20"><path d="M10 4a4 4 0 0 1 4 4c0 3-4 8-4 8s-4-5-4-8a4 4 0 0 1 4-4z" fill="#fff"/></svg></div>
  <div class="f-text" style="left:360px;top:168px">48 Quarry Lane, Suite 3,<br>Basinfield 00421</div>

  <svg class="abs" style="left:485px;top:70px" width="2" height="180"><line x1="1" y1="0" x2="1" y2="180" stroke="#3a4d7a"/></svg>
  <h6 style="left:527px">MAIN LINK</h6>
  <div class="f-link" style="left:534px;top:101px">Home</div>
  <div class="f-link" style="left:534px;top:120px">Doing business here</div>
  <div class="f-link" style="left:534px;top:140px">Living here</div>
  <div class="f-link" style="left:534px;top:160px">Resources &amp; data</div>
  <div class="f-link" style="left:534px;top:180px">Talent &amp; workforce</div>
  <div class="f-link" style="left:534px;top:200px">About RGAUB</div>
  <div class="f-link" style="left:534px;top:220px">Contact Us</div>

  <svg class="abs" style="left:660px;top:70px" width="2" height="180"><line x1="1" y1="0" x2="1" y2="180" stroke="#3a4d7a"/></svg>
  <h6 style="left:707px">TRUSTED BY</h6>
  <div class="abs" style="left:712px;top:104px;width:80px;height:42px;background:#3a4d7a"></div>
  <div class="abs" style="left:716px;top:170px;width:48px;height:48px;border-radius:50%;background:#8a1f2a"></div>

  <svg class="abs" style="left:835px;top:70px" width="2" height="180"><line x1="1" y1="0" x2="1" y2="180" stroke="#3a4d7a"/></svg>
  <h6 style="left:877px">SUBSCRIBE NEWSLETTER</h6>
  <div class="abs" style="left:882px;top:100px;width:195px;height:38px;border:1px solid #fff;background:#fff;color:var(--ink);font-size:10px;padding:12px 12px">Enter Your Email</div>
  <span class="btn" style="left:882px;top:152px;width:135px;height:40px">SUBSCRIBE</span>

  <div class="f-link" style="left:0;width:1200px;text-align:center;top:298px">Copyright © 2025 | Regional Growth Alliance of Upper Basinfield All Right Reserved</div>
</footer>

</body>
</html>
```